Dental Medical History Form - Content provided

Design a medical history form for a dental practice. Content is provided so all that is needed is the formatting to make it look great and easy to read.

"Patient Information" to include all information contained in top portion of the "Patient Medical History Form" docx file.

"Medical History" should follow the formatting and content of the "Exact Medical History" file as this is what the entry fields look like in our practice software and so we would like it to match.

1st page - Patient info, allergies, medications, antibiotics, joint replacement, pregnancy.

2nd page - Do you have, or have you had, any of the following? . . . . . . .
Updates

Project Deadline Extended Reason: Picked too short of a deadline to start (2 days) Added Monday, February 13, 2017

Target Market(s)

All ages but must be clear enough for elderly to read. Use as much space as possible to keep font size bigger yet keep to two pages

Industry/Entity Type

Dental

Font styles to use
Sans Serif

Requirements
Must have
• All content provided
• Our logo at the top (file provided)
• Century Gothic Font
• Limit to two pages

```html
<!DOCTYPE html>
<html lang="en">
<head>
<meta charset="utf-8">
<title>Medical History Form</title>
<link href="https://fonts.googleapis.com/css2?family=Didact+Gothic&display=swap" rel="stylesheet">
<style>
  :root {
    --ink: #111111;
    --rule: #8a8a8a;
    --paper: #ffffff;
    --dots: #9a9a9a;
  }
  * { margin: 0; padding: 0; box-sizing: border-box; }
  html, body { width: 854px; height: 1200px; overflow: hidden; background: var(--paper); }
  body { font-family: "Didact Gothic", "Century Gothic", sans-serif; color: var(--ink); position: relative; }

  .form-title { position: absolute; left: 32px; top: 28px; font-size: 22.5px; font-weight: 400; letter-spacing: 0.1px; }
  .title-rule { position: absolute; left: 32px; top: 53px; width: 800px; border-top: 1px solid var(--rule); }

  .section { position: absolute; width: 394px; }
  .section.left { left: 32px; }
  .section.right { left: 440px; width: 392px; }
  .section-head { font-size: 16px; height: 20px; line-height: 20px; border-bottom: 1px solid var(--rule); padding-left: 0; }
  .section-head.ruled-top { border-top: 1px solid var(--rule); }
  .section-head.ruled-top { padding-top: 6px; height: 27px; }

  .row { position: relative; height: var(--h, 28px); font-size: 13.8px; }
  .row > span { position: absolute; top: 50%; transform: translateY(-50%); white-space: nowrap; }
  .label { left: 1px; }
  .label.two-line { white-space: normal; line-height: 11px; width: 250px; }
  .yes { left: 260px; }
  .no { left: 330px; }
  .tick { width: 21px; height: 21px; border: 1.6px solid var(--ink); border-radius: 50%; }
  .tick.first { left: 288px; }
  .tick.second { left: 358px; }

  .other-field { position: absolute; left: 440px; top: 1069px; font-size: 14px; }
  .fill-line { position: absolute; left: 488px; width: 336px; border-top: 1px dashed var(--dots); }

  .closing-note { position: absolute; right: 32px; top: 1115px; width: 300px; text-align: right; font-size: 11.2px; line-height: 12.6px; }

  .signoff { position: absolute; left: 32px; top: 1070px; width: 395px; height: 98px; border: 1.5px solid var(--ink); }
  .signoff .declaration { position: absolute; left: 13px; top: 5px; font-size: 7px; }
  .signoff .field-name { position: absolute; top: 24px; font-size: 10.5px; }
  .signoff .sig-name { left: 13px; }
  .signoff .date-name { left: 257px; }
  .signoff .sig-line { position: absolute; left: 13px; top: 86px; width: 185px; border-top: 1px dashed var(--dots); }
  .signoff .date-line { position: absolute; left: 257px; top: 86px; width: 134px; border-top: 1px dashed var(--dots); }
  .signoff .slash { position: absolute; top: 66px; font-size: 18px; }
</style>
</head>
<body>

<h1 class="form-title">Do you have, or have you had, any of the following ?</h1>
<div class="title-rule"></div>

<!-- DENTAL -->
<section class="section left" style="top:57px">
  <div class="section-head">DENTAL</div>
  <div style="--h:28.1px">
    <div class="row"><span class="label">Acid Reflux</span><span class="yes">Yes</span><span class="tick first"></span><span class="no">No</span><span class="tick second"></span></div>
    <div class="row"><span class="label">Bad Breath/Taste</span><span class="yes">Yes</span><span class="tick first"></span><span class="no">No</span><span class="tick second"></span></div>
    <div class="row"><span class="label">Bleeding/Swollen/Sore Gums</span><span class="yes">Yes</span><span class="tick first"></span><span class="no">No</span><span class="tick second"></span></div>
    <div class="row"><span class="label">Blisters/Ulcers in Mouth</span><span class="yes">Yes</span><span class="tick first"></span><span class="no">No</span><span class="tick second"></span></div>
    <div class="row"><span class="label">Broken tooth/filling</span><span class="yes">Yes</span><span class="tick first"></span><span class="no">No</span><span class="tick second"></span></div>
    <div class="row"><span class="label">Burning tongue</span><span class="yes">Yes</span><span class="tick first"></span><span class="no">No</span><span class="tick second"></span></div>
    <div class="row"><span class="label">Dry mouth</span><span class="yes">Yes</span><span class="tick first"></span><span class="no">No</span><span class="tick second"></span></div>
    <div class="row"><span class="label">Food collection between teeth</span><span class="yes">Yes</span><span class="tick first"></span><span class="no">No</span><span class="tick second"></span></div>
    <div class="row"><span class="label">Grinding/clenching teeth (day/night)</span><span class="yes">Yes</span><span class="tick first"></span><span class="no">No</span><span class="tick second"></span></div>
    <div class="row"><span class="label">Loose teeth</span><span class="yes">Yes</span><span class="tick first"></span><span class="no">No</span><span class="tick second"></span></div>
    <div class="row"><span class="label">Crooked teeth</span><span class="yes">Yes</span><span class="tick first"></span><span class="no">No</span><span class="tick second"></span></div>
    <div class="row"><span class="label">Discoloured teeth</span><span class="yes">Yes</span><span class="tick first"></span><span class="no">No</span><span class="tick second"></span></div>
    <div class="row"><span class="label">Sensitivity to Hot/Cold</span><span class="yes">Yes</span><span class="tick first"></span><span class="no">No</span><span class="tick second"></span></div>
    <div class="row"><span class="label">Tooth pain when chewing</span><span class="yes">Yes</span><span class="tick first"></span><span class="no">No</span><span class="tick second"></span></div>
    <div class="row"><span class="label">Jaw pain/Fracture</span><span class="yes">Yes</span><span class="tick first"></span><span class="no">No</span><span class="tick second"></span></div>
    <div class="row"><span class="label">Orthodontic treatment/history</span><span class="yes">Yes</span><span class="tick first"></span><span class="no">No</span><span class="tick second"></span></div>
    <div class="row"><span class="label">Oral Cancer</span><span class="yes">Yes</span><span class="tick first"></span><span class="no">No</span><span class="tick second"></span></div>
  </div>
</section>

<!-- DIET / LIFESTYLE -->
<section class="section left" style="top:558px">
  <div class="section-head ruled-top">DIET / LIFESTYLE</div>
  <div style="--h:28px">
    <div class="row"><span class="label two-line">Drink more than one glass alcohol per day</span><span class="yes">Yes</span><span class="tick first"></span><span class="no">No</span><span class="tick second"></span></div>
    <div class="row"><span class="label">Smoking</span><span class="yes">Yes</span><span class="tick first"></span><span class="no">No</span><span class="tick second"></span></div>
    <div class="row"><span class="label">Carbonated drinks</span><span class="yes">Yes</span><span class="tick first"></span><span class="no">No</span><span class="tick second"></span></div>
    <div class="row"><span class="label">Sugary foods</span><span class="yes">Yes</span><span class="tick first"></span><span class="no">No</span><span class="tick second"></span></div>
  </div>
</section>

<!-- BLOOD -->
<section class="section left" style="top:729px">
  <div class="section-head ruled-top">BLOOD</div>
  <div style="--h:28px">
    <div class="row"><span class="label">Anaemia</span><span class="yes">Yes</span><span class="tick first"></span><span class="no">No</span><span class="tick second"></span></div>
    <div class="row"><span class="label">Blood clots</span><span class="yes">Yes</span><span class="tick first"></span><span class="no">No</span><span class="tick second"></span></div>
    <div class="row"><span class="label">Leukemia</span><span class="yes">Yes</span><span class="tick first"></span><span class="no">No</span><span class="tick second"></span></div>
    <div class="row"><span class="label">Low platelets</span><span class="yes">Yes</span><span class="tick first"></span><span class="no">No</span><span class="tick second"></span></div>
    <div class="row"><span class="label">Lymphoma</span><span class="yes">Yes</span><span class="tick first"></span><span class="no">No</span><span class="tick second"></span></div>
    <div class="row"><span class="label">Haemophelia</span><span class="yes">Yes</span><span class="tick first"></span><span class="no">No</span><span class="tick second"></span></div>
  </div>
</section>

<!-- CHEST -->
<section class="section left" style="top:925px">
  <div class="section-head ruled-top">CHEST</div>
  <div style="--h:25.4px">
    <div class="row"><span class="label">Bronchitis</span><span class="yes">Yes</span><span class="tick first"></span><span class="no">No</span><span class="tick second"></span></div>
    <div class="row"><span class="label">Cystic Fibrosis</span><span class="yes">Yes</span><span class="tick first"></span><span class="no">No</span><span class="tick second"></span></div>
    <div class="row"><span class="label">Emphysema</span><span class="yes">Yes</span><span class="tick first"></span><span class="no">No</span><span class="tick second"></span></div>
    <div class="row"><span class="label">Pneumonia</span><span class="yes">Yes</span><span class="tick first"></span><span class="no">No</span><span class="tick second"></span></div>
  </div>
</section>

<!-- INFECTIOUS DISEASE -->
<section class="section right" style="top:57px">
  <div class="section-head">INFECTIOUS DISEASE</div>
  <div style="--h:26.7px">
    <div class="row"><span class="label">Creutzfeldt-Jakob Disease</span><span class="yes">Yes</span><span class="tick first"></span><span class="no">No</span><span class="tick second"></span></div>
    <div class="row"><span class="label">Hepatitis A,B,C,D</span><span class="yes">Yes</span><span class="tick first"></span><span class="no">No</span><span class="tick second"></span></div>
    <div class="row"><span class="label">HIV/AIDS</span><span class="yes">Yes</span><span class="tick first"></span><span class="no">No</span><span class="tick second"></span></div>
    <div class="row"><span class="label">Influenza</span><span class="yes">Yes</span><span class="tick first"></span><span class="no">No</span><span class="tick second"></span></div>
    <div class="row"><span class="label">Shingles</span><span class="yes">Yes</span><span class="tick first"></span><span class="no">No</span><span class="tick second"></span></div>
    <div class="row"><span class="label">Tuberculosis</span><span class="yes">Yes</span><span class="tick first"></span><span class="no">No</span><span class="tick second"></span></div>
  </div>
</section>

<!-- HEART -->
<section class="section right" style="top:241px">
  <div class="section-head ruled-top">HEART</div>
  <div style="--h:23.9px">
    <div class="row"><span class="label">Angina</span><span class="yes">Yes</span><span class="tick first"></span><span class="no">No</span><span class="tick second"></span></div>
    <div class="row"><span class="label">Atrial Fibrillation</span><span class="yes">Yes</span><span class="tick first"></span><span class="no">No</span><span class="tick second"></span></div>
    <div class="row"><span class="label">Blood Pressure (High/Low)</span><span class="yes">Yes</span><span class="tick first"></span><span class="no">No</span><span class="tick second"></span></div>
    <div class="row"><span class="label">Congenital Heart Disease</span><span class="yes">Yes</span><span class="tick first"></span><span class="no">No</span><span class="tick second"></span></div>
    <div class="row"><span class="label">Heart Attack</span><span class="yes">Yes</span><span class="tick first"></span><span class="no">No</span><span class="tick second"></span></div>
    <div class="row"><span class="label">Heart Murmur</span><span class="yes">Yes</span><span class="tick first"></span><span class="no">No</span><span class="tick second"></span></div>
    <div class="row"><span class="label">Heart Surgery</span><span class="yes">Yes</span><span class="tick first"></span><span class="no">No</span><span class="tick second"></span></div>
    <div class="row"><span class="label">Heart Valve Replacement</span><span class="yes">Yes</span><span class="tick first"></span><span class="no">No</span><span class="tick second"></span></div>
    <div class="row"><span class="label">Infective endocarditis</span><span class="yes">Yes</span><span class="tick first"></span><span class="no">No</span><span class="tick second"></span></div>
    <div class="row"><span class="label">Rheumatic Heart Disease</span><span class="yes">Yes</span><span class="tick first"></span><span class="no">No</span><span class="tick second"></span></div>
    <div class="row"><span class="label">Pacemaker</span><span class="yes">Yes</span><span class="tick first"></span><span class="no">No</span><span class="tick second"></span></div>
    <div class="row"><span class="label">Stent</span><span class="yes">Yes</span><span class="tick first"></span><span class="no">No</span><span class="tick second"></span></div>
  </div>
</section>

<!-- OTHER -->
<section class="section right" style="top:561px">
  <div class="section-head ruled-top">OTHER</div>
  <div style="--h:25.4px">
    <div class="row"><span class="label">Anxiety/PTSD</span><span class="yes">Yes</span><span class="tick first"></span><span class="no">No</span><span class="tick second"></span></div>
    <div class="row"><span class="label">Arthritis</span><span class="yes">Yes</span><span class="tick first"></span><span class="no">No</span><span class="tick second"></span></div>
    <div class="row"><span class="label">Alzheimer’s</span><span class="yes">Yes</span><span class="tick first"></span><span class="no">No</span><span class="tick second"></span></div>
    <div class="row"><span class="label">Asthma</span><span class="yes">Yes</span><span class="tick first"></span><span class="no">No</span><span class="tick second"></span></div>
    <div class="row"><span class="label">Anaphylaxis</span><span class="yes">Yes</span><span class="tick first"></span><span class="no">No</span><span class="tick second"></span></div>
    <div class="row"><span class="label">Auto-immune disease</span><span class="yes">Yes</span><span class="tick first"></span><span class="no">No</span><span class="tick second"></span></div>
    <div class="row"><span class="label">Coeliac</span><span class="yes">Yes</span><span class="tick first"></span><span class="no">No</span><span class="tick second"></span></div>
    <div class="row"><span class="label">Depression</span><span class="yes">Yes</span><span class="tick first"></span><span class="no">No</span><span class="tick second"></span></div>
    <div class="row"><span class="label">Diabetes</span><span class="yes">Yes</span><span class="tick first"></span><span class="no">No</span><span class="tick second"></span></div>
    <div class="row"><span class="label">Epilepsy</span><span class="yes">Yes</span><span class="tick first"></span><span class="no">No</span><span class="tick second"></span></div>
    <div class="row"><span class="label">Kidney Disease</span><span class="yes">Yes</span><span class="tick first"></span><span class="no">No</span><span class="tick second"></span></div>
    <div class="row"><span class="label">Liver Disease</span><span class="yes">Yes</span><span class="tick first"></span><span class="no">No</span><span class="tick second"></span></div>
    <div class="row"><span class="label">Osteoporosis</span><span class="yes">Yes</span><span class="tick first"></span><span class="no">No</span><span class="tick second"></span></div>
    <div class="row"><span class="label">Parkinson’s</span><span class="yes">Yes</span><span class="tick first"></span><span class="no">No</span><span class="tick second"></span></div>
    <div class="row"><span class="label">Radiation to Head/Neck</span><span class="yes">Yes</span><span class="tick first"></span><span class="no">No</span><span class="tick second"></span></div>
    <div class="row"><span class="label">Schizophrenia</span><span class="yes">Yes</span><span class="tick first"></span><span class="no">No</span><span class="tick second"></span></div>
    <div class="row"><span class="label">Snoring</span><span class="yes">Yes</span><span class="tick first"></span><span class="no">No</span><span class="tick second"></span></div>
    <div class="row"><span class="label">Sleep apnea</span><span class="yes">Yes</span><span class="tick first"></span><span class="no">No</span><span class="tick second"></span></div>
    <div class="row"><span class="label">Stroke</span><span class="yes">Yes</span><span class="tick first"></span><span class="no">No</span><span class="tick second"></span></div>
  </div>
</section>

<div class="other-field">Other</div>
<div class="fill-line" style="top:1088px"></div>
<div class="fill-line" style="top:1110px"></div>

<p class="closing-note">Thank you for the time to complete your medical history form. Oral health is linked to overall health and this comprehensive questionnaire will help us to provide you with optimal and safe care.</p>

<div class="signoff">
  <span class="declaration">I hereby acknowledge that the above information is correct</span>
  <span class="field-name sig-name">SIGNATURE &nbsp;&nbsp;&nbsp;&nbsp;&nbsp;:</span>
  <span class="field-name date-name">DATE</span>
  <div class="sig-line"></div>
  <div class="date-line"></div>
  <span class="slash" style="left:301px">/</span>
  <span class="slash" style="left:341px">/</span>
</div>

</body>
</html>
```